Design an infographic - a business case for a water sensitive city

Our company is a research organisation - see www.greenharbourliving.org.au. Our work is focused on the re-design of cities to make them more sustainable and liveable, with water as the catalyst.

One of the keys to successful implementation of our research ideas is the 'business case' that demonstrates to decision makers that the benefits of this approach to water management outweigh the costs (it usually costs extra!).

We have realised that traditional business case approaches wont cut it because they focus on the cheapest option, not the one that best satisfies community needs. So a new approach is needed. This is the focus of the infographic. It will highlight the crucial questions to ask (and answer obviously!) in a business case and importantly will highlight a few of the benefits. Statistics emerging from our research have been included to back this up.

The infographic will be used as a marketing and stakeholder engagement piece, so will be included in presentations, annual reports as well as posters.

The web site gives a feel for the corporate colour scheme however style is open to new ideas.

The attached powerpoint file shows five separate but linked concepts that should be included in the infographic. 1. the drivers/need 2. key questions you need to ask when developing your business case 3 . where/how the answers to these questions fit back into a traditional business case process 4. an overview of the benefits of creating a water sensitive city 5. stats. to show that these benefits are real.

These slides have the content but need a design that is consistent across the ideas and ties them together to make a cohesive infographic.

Industry/Entity Type

Marketing

Colors
0555a3
85abd2
f78f20
faa54b

```html
<!DOCTYPE html>
<html lang="en">
<head>
<meta charset="utf-8">
<title>Business case for a water sensitive city</title>
<link href="https://fonts.googleapis.com/css2?family=Courier+Prime:wght@700&family=Quicksand:wght@400;500;700&family=Oswald:wght@300;400;600&display=swap" rel="stylesheet">
<style>
:root{
  --blue:#0555a3;
  --sky:#2f8fd6;
  --lightblue:#85abd2;
  --orange:#f78f20;
  --amber:#faa54b;
  --teal:#1c5f55;
  --teal-light:#b9d3cf;
  --ink:#2e2e30;
  --paper:#eef0f2;
  --slate:#38383a;
  --backdrop:#1f1f20;
  --grey:#646468;
  --node:#6a6a6e;
}
*{margin:0;padding:0;box-sizing:border-box}
html,body{width:1200px;height:1000px;overflow:hidden;background:var(--backdrop)}
body{font-family:"Quicksand",sans-serif;color:var(--ink)}
.canvas{position:relative;width:1200px;height:1000px}
.poster{position:absolute;left:118px;top:0;width:952px;height:1000px;background:var(--paper);overflow:hidden}
.abs{position:absolute}
.rule{position:absolute;height:2px;background:var(--ink)}
.title{position:absolute;left:0;width:952px;top:20px;text-align:center;font-family:"Courier Prime",monospace;font-weight:700;font-size:38px;color:var(--orange);letter-spacing:-1px}
.subtitle{position:absolute;left:0;width:952px;top:60px;text-align:center;font-size:12.5px;color:var(--orange);font-weight:500}
.stat{position:absolute;top:84px;width:210px;height:76px}
.stat svg{position:absolute;left:0;top:0}
.stat .pct{position:absolute;left:0;top:0;width:72px;height:72px;line-height:72px;text-align:center;font-family:"Oswald",sans-serif;font-weight:400;font-size:19px;color:var(--teal)}
.stat .head{position:absolute;left:76px;top:4px;font-weight:700;font-size:11.5px;color:var(--teal);white-space:nowrap}
.stat .body{position:absolute;left:76px;top:18px;font-size:10px;line-height:13px;color:var(--ink);width:125px}
.question{position:absolute;top:175px;left:0;width:952px;text-align:center;font-size:17px;color:var(--ink);white-space:nowrap}
.bar{position:absolute;top:176px;height:19px;background:var(--slate)}
.cloud{position:absolute;background:#c9cbce;border-radius:10px 10px 2px 2px;height:10px}
.section-tab{position:absolute;height:32px;background:var(--sky);color:#fff;font-family:"Oswald",sans-serif;font-weight:300;line-height:32px;padding:0 8px;white-space:nowrap}
.section-shadow{position:absolute;height:30px;background:#dcdee1}
.skyline{position:absolute;background:linear-gradient(180deg,rgba(190,205,220,0),rgba(180,196,214,.55))}
.divider{position:absolute;left:472px;top:266px;width:1px;height:372px;background:#b7bbc0}
svg text{font-family:"Quicksand",sans-serif}
.dark{position:absolute;left:0;top:638px;width:952px;height:362px;background:var(--slate)}
.benefits-tab{position:absolute;left:35px;top:647px;width:370px;height:52px;background:var(--sky);border-radius:0 0 14px 0;color:#fff;font-family:"Oswald",sans-serif;font-weight:300;font-size:27px;line-height:52px;text-align:center;white-space:nowrap}
.item{position:absolute;width:240px;height:70px}
.item .num{position:absolute;left:0;top:-6px;font-family:"Oswald",sans-serif;font-weight:600;font-size:66px;line-height:70px;color:var(--sky)}
.item .name{position:absolute;left:42px;top:0;font-weight:700;font-size:19px;color:var(--sky);white-space:nowrap}
.item .text{position:absolute;left:42px;top:22px;font-size:11px;line-height:14.5px;color:var(--sky);width:188px}
.examples{position:absolute;left:494px;top:650px;font-family:"Courier Prime",monospace;font-weight:700;font-size:29px;color:var(--orange);white-space:nowrap}
.caption{position:absolute;font-size:10.5px;color:#fff;white-space:nowrap}
.bubble{position:absolute;border-radius:50%;background:#fff;border:5px solid var(--amber);color:var(--amber);font-weight:700;text-align:center;display:flex;align-items:center;justify-content:center;line-height:1.05}
.note{position:absolute;font-size:9.5px;line-height:11.5px;color:var(--amber)}
</style>
</head>
<body>
<div class="canvas">
<div class="poster">

  <div class="rule" style="left:75px;top:46px;width:247px"></div>
  <div class="rule" style="left:627px;top:46px;width:248px"></div>
  <h1 class="title">Communities</h1>
  <p class="subtitle">are calling for new water services in our cities</p>

  <div class="stat" style="left:80px">
    <svg width="72" height="72" viewBox="0 0 72 72"><circle cx="36" cy="36" r="29" fill="none" stroke="var(--teal-light)" stroke-width="13"/><circle cx="36" cy="36" r="29" fill="none" stroke="var(--teal)" stroke-width="13" stroke-dasharray="109.3 182.2" transform="rotate(-90 36 36)"/></svg>
    <div class="pct">60%</div>
    <div class="head">of householders</div>
    <div class="body">think of themselves as being environmentally sustainable</div>
  </div>
  <div class="stat" style="left:277px">
    <svg width="72" height="72" viewBox="0 0 72 72"><circle cx="36" cy="36" r="29" fill="none" stroke="var(--teal-light)" stroke-width="13"/><circle cx="36" cy="36" r="29" fill="none" stroke="var(--teal)" stroke-width="13" stroke-dasharray="94 182.2" transform="rotate(-90 36 36)"/></svg>
    <div class="pct">&gt;50%</div>
    <div class="head">of people support</div>
    <div class="body">installation of rain gardens in their street, preferring this to rain gardens on their own property</div>
  </div>
  <div class="stat" style="left:488px">
    <svg width="72" height="72" viewBox="0 0 72 72"><circle cx="36" cy="36" r="29" fill="none" stroke="var(--teal-light)" stroke-width="13"/><circle cx="36" cy="36" r="29" fill="none" stroke="var(--teal)" stroke-width="13" stroke-dasharray="63.8 182.2" transform="rotate(90 36 36)"/></svg>
    <div class="pct">~35%</div>
    <div class="head">of people object</div>
    <div class="body">to the use of desalinated water for non-drinking purposes</div>
  </div>
  <div class="stat" style="left:692px">
    <svg width="72" height="72" viewBox="0 0 72 72"><circle cx="36" cy="36" r="29" fill="none" stroke="var(--teal-light)" stroke-width="13"/><circle cx="36" cy="36" r="29" fill="none" stroke="var(--teal)" stroke-width="13" stroke-dasharray="145.8 182.2" transform="rotate(-90 36 36)"/></svg>
    <div class="pct">~80%</div>
    <div class="head">of householders</div>
    <div class="body">say they are willing to use recycled water for non-drinking purposes in the home</div>
  </div>

  <div class="cloud" role="img" aria-label="Small cloud" style="left:563px;top:158px;width:50px"></div>
  <div class="cloud" role="img" aria-label="Small cloud" style="left:28px;top:202px;width:42px"></div>
  <div class="cloud" role="img" aria-label="Small cloud" style="left:768px;top:208px;width:48px"></div>

  <div class="bar" style="left:74px;width:165px"></div>
  <div class="bar" style="left:711px;width:164px"></div>
  <p class="question">...but how are these intentions built into a business case?</p>

  <div class="section-shadow" style="left:50px;top:238px;width:240px"></div>
  <div class="section-tab" style="left:92px;top:233px;font-size:20px">5 key things to know</div>
  <div class="section-shadow" style="left:522px;top:240px;width:350px"></div>
  <div class="section-tab" style="left:562px;top:235px;font-size:18px">Where do I include these in a business case ?</div>

  <div class="skyline" role="img" aria-label="Faint city skyline illustration behind the diagrams" style="left:0;top:380px;width:472px;height:258px"></div>
  <div class="skyline" role="img" aria-label="Faint city skyline illustration with coloured towers" style="left:700px;top:490px;width:252px;height:148px"></div>
  <div class="divider"></div>

  <svg class="abs" style="left:0;top:270px" width="472" height="368" viewBox="0 0 472 368">
    <g fill="var(--grey)">
      <path d="M30 44 L102 38 L104 116 L36 110 Z"/>
      <path d="M284 20 L330 12 L332 46 L286 50 Z"/>
      <path d="M372 72 L450 62 L454 146 L378 134 Z"/>
      <path d="M36 192 L126 200 L124 280 L40 272 Z"/>
      <path d="M336 214 L420 220 L418 308 L338 296 Z"/>
    </g>
    <g fill="#fff" font-size="6.5">
      <text x="34" y="57" font-weight="700">Who will pay?</text>
      <text x="42" y="75">Utilities</text><text x="42" y="83">Councils</text><text x="42" y="91">Home owners</text><text x="42" y="99">Developers</text>
      <text x="288" y="26" font-size="5.5">Which option has</text><text x="288" y="33" font-size="5.5">the lowest</text><text x="288" y="40" font-size="5.5">community cost?</text>
      <text x="380" y="82" font-weight="700">Who benefits?</text>
      <text x="382" y="93">Local communities</text><text x="382" y="100">Home owners</text><text x="382" y="107">Utilities</text><text x="382" y="114">Councils</text><text x="382" y="121">Developers</text><text x="382" y="128">Government</text>
      <text x="40" y="206" font-weight="700" font-size="6">What are the changes to</text><text x="40" y="213" font-weight="700" font-size="6">the water cycle?</text>
      <text x="50" y="230">Green infrastructure</text><text x="50" y="237">Water conservation</text><text x="50" y="244">Reduced runoff</text><text x="50" y="251">Water supplies</text><text x="50" y="258">Urban cooling</text><text x="50" y="265">Resources &amp; energy</text><text x="50" y="272">Flood protection</text>
      <text x="340" y="228" font-weight="700" font-size="6">What does it mean for the</text><text x="340" y="235" font-weight="700" font-size="6">community?</text>
      <text x="346" y="252">Safety</text><text x="346" y="259">Cleaner rivers</text><text x="346" y="266">Better health</text><text x="346" y="273">Sustainability</text><text x="346" y="280">Ecosystem services</text><text x="346" y="287">Developer returns</text><text x="346" y="294">Savings (water cost)</text>
    </g>
    <path d="M196 88 L238 88 L270 120 L160 120 Z" fill="var(--orange)"/>
    <path d="M152 130 Q232 94 318 130 L320 168 Q300 200 232 214 Q168 200 146 168 Z" fill="var(--sky)"/>
    <text x="215" y="112" fill="#fff" font-size="11.5" text-anchor="middle">The life cycle</text>
    <text x="232" y="168" fill="#fff" font-size="15" text-anchor="middle">The benefits</text>
    <g stroke="#fff" stroke-width="1.2" stroke-dasharray="3 2" fill="none">
      <path d="M210 235 L244 235"/>
    </g>
    <g fill="#fff" stroke="var(--sky)" stroke-width="6">
      <circle cx="232" cy="55" r="40"/><circle cx="139" cy="128" r="40"/><circle cx="323" cy="128" r="40"/><circle cx="170" cy="226" r="40"/><circle cx="284" cy="226" r="40"/>
    </g>
    <g fill="var(--ink)" font-weight="700" font-size="13" text-anchor="middle">
      <text x="232" y="56">Community</text><text x="232" y="73">cost</text>
      <text x="139" y="133">Funders</text>
      <text x="323" y="132" font-size="11.5">Beneficiaries</text>
      <text x="170" y="214">Water</text><text x="170" y="230">cycle</text><text x="170" y="246">benefits</text>
      <text x="284" y="221">Broader</text><text x="284" y="237">city</text><text x="284" y="253">benefits</text>
    </g>
  </svg>

  <svg class="abs" style="left:473px;top:270px" width="479" height="368" viewBox="0 0 479 368">
    <g stroke="var(--lightblue)" stroke-width="1" fill="none">
      <path d="M208 35 L92 35 L92 69"/>
      <path d="M92 50 L35 50 L35 171"/>
      <path d="M262 35 L384 35 L384 64"/>
      <path d="M92 89 L92 97 L142 97 L142 102"/>
      <path d="M142 118 L142 130 L129 130 L129 141"/>
      <path d="M129 157 L129 166 L157 166 L157 172"/>
      <path d="M157 190 L157 202 L93 202 L93 210"/>
      <path d="M35 191 L35 219 L63 219"/>
      <path d="M70 228 L39 228 L39 244"/>
      <path d="M116 228 L147 228 L147 244"/>
      <path d="M39 260 L39 286 L63 286"/>
      <path d="M147 260 L147 286 L119 286"/>
      <path d="M91 295 L91 308"/>
      <path d="M111 322 L147 322 L147 322"/>
      <path d="M120 82 L366 82"/>
      <path d="M170 110 L251 110"/>
      <path d="M157 148 L220 148"/>
      <path d="M123 219 L197 219"/>
      <path d="M119 286 L210 286"/>
      <path d="M384 98 L384 113 L291 113"/>
      <path d="M271 133 L254 142"/>
      <path d="M284 126 L296 163"/>
      <path d="M296 199 L296 222 L233 222"/>
      <path d="M215 240 L215 277"/>
      <path d="M111 322 L120 330"/>
    </g>
    <g fill="var(--lightblue)" font-size="5.5">
      <text x="245" y="80">Feeds into</text><text x="245" y="88">...</text>
      <text x="180" y="108">Feeds into</text><text x="180" y="116">...</text>
      <text x="162" y="146">Feeds into</text><text x="162" y="154">...</text>
      <text x="150" y="217">Feeds into</text><text x="150" y="225">...</text>
      <text x="125" y="284">Feeds into</text><text x="125" y="292">...</text>
    </g>
    <g fill="var(--ink)" font-size="5.5"><text x="80" y="200">Modelling</text><text x="42" y="234">NPV</text><text x="132" y="234">Multi criteria</text></g>
    <text x="89" y="33" fill="var(--blue)" font-size="8" font-weight="700">No</text>
    <text x="274" y="33" fill="var(--blue)" font-size="7.5">Yes – include the following</text>
    <g fill="var(--blue)">
      <circle cx="235" cy="35" r="27"/><circle cx="384" cy="82" r="18"/><circle cx="271" cy="113" r="20"/><circle cx="237" cy="148" r="17"/><circle cx="296" cy="181" r="18"/><circle cx="215" cy="222" r="18"/>
      <rect x="210" y="277" width="54" height="18" rx="2"/>
    </g>
    <g fill="#fff" font-size="6.5" text-anchor="middle">
      <text x="235" y="24">Water</text><text x="235" y="32">sensitive city</text><text x="235" y="40">business</text><text x="235" y="48">case?</text>
      <text x="384" y="80">Threats to</text><text x="384" y="88">cities</text>
      <text x="271" y="107">Sustainable</text><text x="271" y="115">liveable</text><text x="271" y="123">resilient</text>
      <text x="237" y="150">Benefits</text>
      <text x="296" y="179">Engage</text><text x="296" y="187">beneficiaries</text>
      <text x="215" y="220">Lifecycle</text><text x="215" y="228">costs</text>
      <text x="237" y="288">Community cost</text>
    </g>
    <g fill="var(--blue)" font-size="5.3"><text x="410" y="58">Droughts</text><text x="410" y="65">Flooding</text><text x="410" y="72">Reduced liveability</text><text x="410" y="79">Affordability</text><text x="410" y="86">Heatwaves</text><text x="410" y="93">Densification</text><text x="410" y="100">Population growth</text><text x="410" y="107">Aging infrastructure</text></g>
    <text x="294" y="109" fill="var(--blue)" font-size="4.8" font-style="italic">A vision for a water sensitive city</text>
    <g fill="var(--node)">
      <ellipse cx="92" cy="79" rx="26" ry="10"/><ellipse cx="142" cy="110" rx="27" ry="8"/><ellipse cx="129" cy="149" rx="27" ry="8"/><ellipse cx="157" cy="181" rx="27" ry="9"/><ellipse cx="35" cy="181" rx="27" ry="10"/><ellipse cx="93" cy="219" rx="30" ry="9"/><ellipse cx="39" cy="252" rx="24" ry="8"/><ellipse cx="147" cy="252" rx="24" ry="8"/><ellipse cx="91" cy="286" rx="28" ry="9"/><ellipse cx="91" cy="318" rx="24" ry="10"/><ellipse cx="147" cy="330" rx="24" ry="8"/>
    </g>
    <g fill="#fff" font-size="6.2" text-anchor="middle">
      <text x="92" y="77">Define the</text><text x="92" y="85">problem</text>
      <text x="142" y="112">Set objectives</text><text x="129" y="151">Define criteria</text><text x="157" y="183">Identify options</text>
      <text x="35" y="179">Define business</text><text x="35" y="187">as usual</text>
      <text x="93" y="221">Evaluate options</text><text x="39" y="254">Financial</text><text x="147" y="254">Intangible</text>
      <text x="91" y="288">Decision making</text><text x="91" y="316">Preferred</text><text x="91" y="324">option</text><text x="147" y="332">Funding</text>
    </g>
  </svg>

  <div class="dark"></div>
  <div class="benefits-tab">What are some of the benefits?</div>

  <div class="item" style="left:30px;top:741px"><span class="num">1</span><span class="name">Natural systems</span><p class="text">treat pollutants, create a sense of place and provide ecosystem services</p></div>
  <div class="item" style="left:30px;top:813px"><span class="num">2</span><span class="name">Water efficiency</span><p class="text">and growth in alternative supplies reduce the demand for drinking water</p></div>
  <div class="item" style="left:30px;top:887px"><span class="num">3</span><span class="name">Storm water</span><p class="text">and sewerage is managed as a resource rather than a waste. Flows and pollutants are retained</p></div>
  <div class="item" style="left:273px;top:741px"><span class="num">4</span><span class="name">Trees and water</span><p class="text">in the urban landscape reduce temperatures during heat waves</p></div>
  <div class="item" style="left:273px;top:813px"><span class="num">5</span><span class="name">Waste water</span><p class="text">can provide energy, nutrients and minerals</p></div>
  <div class="item" style="left:273px;top:887px"><span class="num">6</span><span class="name">Corridors of green</span><p class="text">and blue throughout cities create space for flood waters when it rains and space for play at other times</p></div>

  <div class="examples">Examples of the benefits</div>

  <svg class="abs" style="left:500px;top:700px" width="452" height="300" viewBox="0 0 452 300">
    <g stroke="var(--amber)" stroke-width="2" fill="none">
      <path d="M52 44 L52 18 L370 18 L370 34"/><path d="M198 18 L198 36"/>
      <path d="M45 200 L45 176 L330 176 L330 184"/>
    </g>
  </svg>
  <p class="caption" style="left:585px;top:699px">Green city + water in the landscape = health benefits</p>
  <p class="caption" style="left:549px;top:855px">Rainwater tanks = financial returns for householders</p>

  <div class="bubble" style="left:530px;top:742px;width:46px;height:46px;font-size:9.5px">0.5-1°C</div>
  <p class="note" style="left:578px;top:770px;width:92px">Reduction in land surface temperature for every 10% increase in tree cover</p>
  <div class="bubble" style="left:681px;top:734px;width:54px;height:54px;font-size:14px">1-2°C</div>
  <p class="note" style="left:742px;top:757px;width:96px">Temperature reduction significantly reduces morbidity &amp; mortality</p>
  <div class="bubble" style="left:833px;top:732px;width:70px;height:70px;font-size:18px">3-5°C</div>
  <p class="note" style="left:818px;top:806px;width:120px">Cooling effect of irrigation in Dubbo town centre, compared with unirrigated surrounding rural land, on a 40oC day</p>

  <div class="bubble" style="left:522px;top:898px;width:60px;height:60px;font-size:14px">$100-<br>$200</div>
  <p class="note" style="left:588px;top:909px;width:120px">Annual saving in household water bills by using a rainwater tank to reduce drinking water use</p>
  <div class="bubble" style="left:762px;top:882px;width:74px;height:74px;font-size:20px">3.7%</div>
  <p class="note" style="left:838px;top:909px;width:110px">Increase in property value (when you sell!) for houses with rainwater tanks</p>
</div>
</div>
</body>
</html>
```